Bulldog themed background for Real Estate Purchase Letter

I need a phantom background or watermark on a standard 8 1/2" x 11" paper. I am going to put a letter over the background. I want a bulldog theme that is cute, funny and original. This letter is for a real estate project and we want to capture the person sub-consciously . Attached is my personal dogs. If you want to use them you can but not required. I have attached the letter that I am trying to emulate. I want bulldogs not horses.

Target Market(s)

45 years old and higher

Industry/Entity Type

Real Estate

Font styles to use
Serif
Sans Serif

Colors

Designer to choose colors to be used in the design.

Requirements
Must have
• fun, happiness, reassuring,
Should not have
• violence, negativity, unhappy

```html
<!DOCTYPE html>
<html lang="en">
<head>
<meta charset="utf-8">
<title>Brindle Homes Letterhead</title>
<link rel="stylesheet" href="https://fonts.googleapis.com/css2?family=Open+Sans:wght@300;400;600&display=swap">
<style>
  :root {
    --brand-red: #ed1c33;
    --ink: #2b2b2b;
    --body-text: #555555;
    --rule-grey: #c8c8c8;
    --paper: #ffffff;
    --tan: #e9cfb0;
    --tan-soft: #f4e6d6;
  }
  * { margin: 0; padding: 0; box-sizing: border-box; }
  html, body { width: 927px; height: 1200px; overflow: hidden; background: var(--paper); }
  body { font-family: "Open Sans", sans-serif; color: var(--body-text); }
  .letterhead { position: relative; width: 927px; height: 1200px; background: var(--paper); overflow: hidden; }

  .brand { position: absolute; left: 120px; top: 84px; display: flex; align-items: center; gap: 10px; }
  .brand-square { width: 26px; height: 26px; background: var(--brand-red); }
  .brand-name { font-size: 28px; font-weight: 600; color: var(--ink); letter-spacing: -0.3px; line-height: 1; }

  .rule { position: absolute; left: 120px; width: 689px; height: 3px; background: var(--rule-grey); }
  .rule::before { content: ""; position: absolute; left: 0; top: 0; width: 65px; height: 3px; background: var(--brand-red); }
  .rule-top { top: 148px; }
  .rule-bottom { top: 1038px; }

  .background-art { position: absolute; left: 110px; top: 173px; width: 700px; height: 848px;
    background: radial-gradient(ellipse at 62% 40%, var(--tan-soft) 0%, #f7ece0 45%, rgba(255,255,255,0) 75%),
                radial-gradient(ellipse at 45% 75%, #f6e9da 0%, rgba(255,255,255,0) 65%);
    opacity: 0.9; }

  .sender { position: absolute; left: 130px; top: 224px; }
  .sender-name { font-size: 15px; color: var(--brand-red); font-weight: 400; line-height: 22px; }
  .sender-title { font-size: 11.5px; color: var(--body-text); line-height: 20px; margin-bottom: 2px; }
  .sender-line { font-size: 14px; font-weight: 300; color: var(--ink); line-height: 22.5px; white-space: nowrap; }
  .sender-line .key { display: inline-block; width: 29px; }
  .sender-line .key.accent { color: var(--brand-red); }

  .date { position: absolute; right: 117px; top: 290px; font-size: 14px; font-weight: 300; color: var(--ink); }

  .letter-body { position: absolute; left: 130px; top: 356px; width: 680px; font-size: 14px; font-weight: 300; color: var(--ink); line-height: 29.7px; }
  .letter-body p { margin-bottom: 29.7px; white-space: nowrap; }

  .signoff { position: absolute; left: 129px; top: 882px; color: var(--ink); font-weight: 300; }
  .signature { font-size: 29px; line-height: 40px; margin-bottom: 8px; }
  .signoff-line { font-size: 13.5px; line-height: 16px; font-weight: 400; }

  .contact-bar { position: absolute; top: 1068px; left: 0; width: 927px; height: 44px; }
  .contact { position: absolute; top: 0; display: flex; align-items: center; }
  .contact svg { display: block; }
  .contact-text { position: absolute; font-size: 13.5px; line-height: 17px; color: var(--ink); white-space: nowrap; top: 6px; }
  .contact-phone { left: 135px; }
  .contact-phone .contact-text { left: 42px; }
  .contact-mail { left: 352px; top: 8px; }
  .contact-mail .contact-text { left: 48px; top: -2px; }
  .contact-place { left: 603px; }
  .contact-place .contact-text { left: 44px; }

  .footer-band { position: absolute; left: 0; top: 1158px; width: 927px; height: 40px; background: var(--brand-red); }
</style>
</head>
<body>
<div class="letterhead">
  <div class="background-art" role="img" aria-label="Faint watermark photograph of a sitting bulldog behind the letter"></div>

  <header class="brand">
    <span class="brand-square"></span>
    <span class="brand-name">Brindle Homes</span>
  </header>
  <div class="rule rule-top"></div>

  <section class="sender">
    <div class="sender-name">Marla Quint</div>
    <div class="sender-title">Chief Director</div>
    <div class="sender-line"><span class="key accent">A :</span>12-3, Linden Row Harbourton - 4417</div>
    <div class="sender-line"><span class="key">W :</span>hello@quintmail.com, www.quintplace.com</div>
    <div class="sender-line"><span class="key accent">P :</span>+555 - 20418 - 3307</div>
  </section>

  <div class="date">Date, 10 September, 2020</div>

  <main class="letter-body">
    <p>This is a sample letter that has been placed to demonstrate typing remat (Your Company). letterhead<br>design. When positioned properly, it will serve to work in harmony with all other elements letterhead.<br>This letterhead design is meant to project an image</p>
    <p>This letterhead design is meant project an image of professionalism reliability. By using simple aligen<br>we have created a very spacious feeling. The simplicity suggest &nbsp;rengththe spaciousnes contributes h<br>aesthetics the layout. These basic qualities along with the (Your Company)</p>
    <p>look and helps reinforce the (Your Company) brand. letterhead design is meant to project an image p<br>design. When positioned properly, it will serve to work in harmony all the other elements letterhead.<br>sionalism and reliability.</p>
    <p>This letterhead design is based on the (Form of your logo) form (Your Company) logo. Each stationery<br>we have created a very spacious feeling. The simplicity suggests strength the spaciousnes contribute<br>part of the (Form of your logo).</p>
  </main>

  <section class="signoff">
    <div class="signature">Marla Quint</div>
    <div class="signoff-line">Marla Quint</div>
    <div class="signoff-line">Manager</div>
  </section>

  <div class="rule rule-bottom"></div>

  <footer class="contact-bar">
    <div class="contact contact-phone">
      <svg width="27" height="40" viewBox="0 0 27 40" aria-hidden="true">
        <rect x="1.5" y="1.5" width="24" height="37" rx="3" fill="none" stroke="var(--brand-red)" stroke-width="2.2"/>
        <line x1="1.5" y1="7" x2="25.5" y2="7" stroke="var(--brand-red)" stroke-width="1.6"/>
        <line x1="1.5" y1="32" x2="25.5" y2="32" stroke="var(--brand-red)" stroke-width="1.6"/>
        <line x1="10" y1="4.3" x2="17" y2="4.3" stroke="var(--brand-red)" stroke-width="1.2"/>
        <circle cx="13.5" cy="35.3" r="1" fill="var(--brand-red)"/>
      </svg>
      <div class="contact-text">+555 010 482 913<br>+555 010 482 913</div>
    </div>
    <div class="contact contact-mail">
      <svg width="35" height="26" viewBox="0 0 35 26" aria-hidden="true">
        <rect x="1.5" y="1.5" width="32" height="23" rx="2" fill="none" stroke="var(--brand-red)" stroke-width="2.2"/>
        <polyline points="2,3 17.5,15 33,3" fill="none" stroke="var(--brand-red)" stroke-width="2"/>
        <line x1="2" y1="24" x2="13" y2="12.5" stroke="var(--brand-red)" stroke-width="1.8"/>
        <line x1="33" y1="24" x2="22" y2="12.5" stroke="var(--brand-red)" stroke-width="1.8"/>
      </svg>
      <div class="contact-text">info@brindlehomes.com<br>marla@brindlehomes.com</div>
    </div>
    <div class="contact contact-place">
      <svg width="30" height="40" viewBox="0 0 30 40" aria-hidden="true">
        <path d="M15 38 C9 30 2 22 2 14 A13 13 0 0 1 28 14 C28 22 21 30 15 38 Z" fill="none" stroke="var(--brand-red)" stroke-width="2.2" stroke-linejoin="round"/>
        <circle cx="15" cy="14" r="6" fill="none" stroke="var(--brand-red)" stroke-width="2"/>
      </svg>
      <div class="contact-text">418 Alder Way<br>Westbrook, USA.</div>
    </div>
  </footer>

  <div class="footer-band"></div>
</div>
</body>
</html>
```